"Freedom" New Year Electronic Card

Velantor is a regulatory consulting company in the cosmetic sector. We provide premium services and have 12 years of experience.

Please visit our website for more information: https://velantor-example.com

We need a graphic for a New Year electronic card to send to our clients (see brief attached):
- The attached picture shows the Holiday card we used before the Christmas break. We like the idea to make drawings with anonymized cosmetic packaging. We would like to do it with "2021".
- You can design a background (with nice shades of colors) but leave space at top and bottom for us to include text in different languages.
- We would like that the "1" of "2021" be a symbol of freedom. We thought about a dandelion and flying seeds (see brief) but you may propose something else (such as birds escaping a cage, broken chains, etc.)

We need something very professional, serious, beautiful and in line with our graphic layout (see our company website).

Target Market(s)

B2B professionals of the cosmetic industry

Requirements
Must have
• Symbol of freedom (dandelion, broken chain, birds escaping a cage, etc.)
Should not have
• Christmas-related things (no christmas trees, etc.)
No medical fatures (no seringes, etc.)

```html
<!DOCTYPE html>
<html lang="en">
<head>
<meta charset="UTF-8">
<title>Velantor – New Year 2021 Card</title>
<link rel="stylesheet" href="https://fonts.googleapis.com/css2?family=Montserrat:wght@400;700&family=Oswald:wght@600&display=swap">
<style>
  :root {
    --page-bg: #e4e2df;
    --accent-green: #9ccf55;
    --text-light: #eef0ec;
    --brand-white: #f4f4f2;
    --bg-teal: #5d7a70;
    --bg-grey: #7a7c7b;
    --bg-olive: #586a3c;
    --bg-warm: #8c8a55;
    --bg-deep: #47583a;
  }
  * { margin: 0; padding: 0; box-sizing: border-box; }
  html, body {
    width: 1200px;
    height: 900px;
    overflow: hidden;
    background: var(--page-bg);
  }
  .card {
    position: absolute;
    left: 0;
    top: 50px;
    width: 1200px;
    height: 800px;
    overflow: hidden;
    font-family: "Montserrat", sans-serif;
  }
  .card-backdrop {
    position: absolute;
    inset: 0;
    background:
      radial-gradient(ellipse 45% 30% at 50% 72%, rgba(140,138,85,0.55), transparent 70%),
      radial-gradient(ellipse 40% 40% at 95% 65%, rgba(71,88,58,0.8), transparent 70%),
      radial-gradient(ellipse 35% 35% at 5% 85%, rgba(88,106,60,0.8), transparent 70%),
      linear-gradient(180deg, var(--bg-teal) 0%, var(--bg-grey) 35%, var(--bg-grey) 50%, var(--bg-olive) 85%, var(--bg-deep) 100%);
  }
  .greeting-text {
    position: absolute;
    top: 42px;
    left: 40px;
    right: 40px;
    text-align: center;
    color: var(--text-light);
    font-size: 18.5px;
    line-height: 27px;
    font-weight: 400;
    white-space: nowrap;
  }
  .year-mark {
    position: absolute;
    left: 0;
    top: 0;
    width: 1200px;
    height: 800px;
  }
  .year-digits {
    font-family: "Oswald", sans-serif;
    font-weight: 600;
    fill: var(--accent-green);
  }
  .freedom-symbol {
    position: absolute;
    left: 906px;
    top: 222px;
    width: 58px;
    height: 390px;
    border-radius: 29px;
    background: linear-gradient(180deg, rgba(156,207,85,0.55), rgba(156,207,85,0.35));
  }
  .brand-name {
    position: absolute;
    left: 0;
    right: 0;
    top: 644px;
    text-align: center;
    color: var(--brand-white);
    font-family: "Montserrat", sans-serif;
    font-weight: 700;
    font-size: 100px;
    line-height: 120px;
    letter-spacing: 0.01em;
  }
</style>
</head>
<body>
  <main class="card">
    <div class="card-backdrop" role="img" aria-label="Soft-focus photograph of a dandelion seed head with seeds drifting against a grey-green sky"></div>

    <p class="greeting-text">
      Lorem ipsum dolor sit amet, consectetuer adipiscing elit, sed diam nonummy nibh euismod tincidunt ut laoreet<br>
      dolore magna aliquam erat volutpat. Ut wisi enim ad minim veniam, quis nostrud exerci tation ullamcorper<br>
      suscipit lobortis nisl ut aliquip ex ea commodo consequat. Duis autem vel elit, sed diam nonummy nibh<br>
      euismod tincidunt ut laoreet
    </p>

    <svg class="year-mark" viewBox="0 0 1200 800" aria-label="2021">
      <text class="year-digits" x="243" y="611" font-size="470" textLength="600" lengthAdjust="spacingAndGlyphs">202</text>
    </svg>

    <div class="freedom-symbol" role="img" aria-label="Green illustration of a vertical broken chain forming the final 1 of 2021"></div>

    <div class="brand-name">Velantor</div>
  </main>
</body>
</html>
```